Tourism Marketing needing sleek, clear design for business card & proposal documents.

***Company background***
"Quiet Harbour" is a company specializing in tourism marketing and project management. We do international wholesale, event management as well as ongoing representation of tourism and hospitality companies.

***Target market***
We cater to tourism companies and hotel professionals.

***Task***
We would like to get a single sided business card designed (but will still consider two sided, we are open to any ideas you may have). The layout for this card should be modern and elegant. Currently we do not have a logo, but we would like our business name in a really simple typography for the business card (similar to Merrow Lounge's logo - www.merrowlounge.com.au).We are after a design that is clear, strong enough to be recognised as Quiet Harbour that does not require any fancy design. Another option is a simple play on QH (Quiet Harbour) or simply have Quiet Harbour featured elsewhere on card more as a brand/logo.

Feel free to submit different fonts if you feel you have any other fonts/designs that may be suitable for this card other than sans serifs. Should this project be successful, we will be considering several other projects for business proposal templates and eventually a website design.

The information that needs to go on the card are as follows:

Odette Farrow
Director
Quiet Harbour
Tourism Marketing & Representation
57 Wendlow Terrace
Prahran, Victoria, 3181 Australia
T +61 428306172 E odette@quietharbour.com.au

***Look and feel***
We'd like the business card design to express the following:
Modern, sleek, elegant, simple, discreet, quality, subtle, professional, creative, innovation

In terms of typography, we like something really simple and blocky (similar font to Merrow Lounge's logo - www.merrowlounge.com.au)

***Colour scheme***
Shades of grey and dark teal

***Note***
Although our main target market are professionals, we would like the business card design to be versatile enough to be used outside of the tourism industry and need to appeal to different markets.

I do not have existing logo. Was hoping for a design that may be clear, strong enough not to require one. Other option is a simple play on QH (Quiet Harbour) or simply have Quiet Harbour featured elsewhere on card more as a brand/logo.

Odette Farrow
Director
Quiet Harbour Pty Ltd 
57 Wendlow Terrace
T +61 428306172  E  odette@quietharbour.com.au

Thank you for designs so far. Many have used a mauve colour which matches our company profile. This is not necessary, as that is just a draft and will be completely redesigned, so dont  feel you need to incorporate the mauve.

My colour preferences are for a white or grey background, and I like fonts in dark teals, grey or other sophisticated but modern colours. feel free to submit different fonts if you you have other fonts you thing would be suitable for this card, along with sans serifs. Should this project be successful, we will be considering several others for business proposal templates and eventually website. 

Target Market(s)

International Hospitality Senior Executives, Directors of International Tourism Companies, Directors of Tourism Bodies Internationally, local Tourism

Industry/Entity Type

Hospitality

Requirements
Should not have
• must not have bright garish colour, swirly patterns or anything that dates too much.

```html
<!DOCTYPE html>
<html lang="en">
<head>
<meta charset="utf-8">
<title>Quiet Harbour — Business Card</title>
<link href="https://fonts.googleapis.com/css2?family=Mulish:wght@300;400;800&display=swap" rel="stylesheet">
<style>
  :root {
    --stage: #a3a5a7;
    --paper: #f7f7f6;
    --brand-deep: #0f5a98;
    --brand-mid: #1688c4;
    --brand-light: #2aa0d6;
    --brand-text: #15639f;
    --tagline: #4a8dc0;
    --ink-white: #ffffff;
    --ink-soft: #d4ecf8;
    --mark-faint: rgba(190, 220, 240, 0.55);
    --web-ink: #3d4c58;
  }
  * { box-sizing: border-box; margin: 0; padding: 0; }
  html, body { width: 1200px; height: 720px; overflow: hidden; }
  body {
    background: var(--stage);
    font-family: "Mulish", "Century Gothic", sans-serif;
    display: flex;
    align-items: center;
    justify-content: center;
    gap: 40px;
  }
  .card {
    position: relative;
    width: 540px;
    height: 310px;
    overflow: hidden;
    box-shadow: 0 8px 22px rgba(0,0,0,0.22);
  }

  /* Front */
  .card--front { background: var(--paper); }
  .brand {
    position: absolute;
    left: 70px;
    top: 92px;
    display: flex;
    align-items: center;
    gap: 16px;
  }
  .brand__square {
    width: 62px;
    height: 62px;
    background: linear-gradient(135deg, var(--brand-light), var(--brand-deep));
  }
  .brand__name {
    font-weight: 800;
    font-size: 40px;
    line-height: 1;
    color: var(--brand-text);
    letter-spacing: 0.5px;
  }
  .front__tagline {
    position: absolute;
    left: 148px;
    top: 146px;
    font-size: 18px;
    font-weight: 400;
    color: var(--tagline);
    white-space: nowrap;
  }
  .front__web {
    position: absolute;
    right: 26px;
    bottom: 22px;
    display: flex;
    align-items: center;
    gap: 8px;
    font-size: 13px;
    color: var(--web-ink);
  }
  .front__web svg { width: 16px; height: 16px; }

  /* Back */
  .card--back {
    background: linear-gradient(160deg, var(--brand-light) 0%, var(--brand-mid) 45%, var(--brand-deep) 100%);
    color: var(--ink-white);
  }
  .back__tab {
    position: absolute;
    left: 18px;
    top: 20px;
    width: 24px;
    height: 22px;
    background: var(--ink-white);
  }
  .back__heading {
    position: absolute;
    left: 56px;
    top: 12px;
    display: flex;
    flex-direction: column;
    align-items: flex-end;
  }
  .back__name {
    font-size: 30px;
    font-weight: 300;
    line-height: 1.2;
  }
  .back__role {
    font-size: 16px;
    font-weight: 300;
    line-height: 1.1;
    margin-top: -2px;
  }
  .back__tagline {
    position: absolute;
    right: 22px;
    top: 104px;
    font-size: 15px;
    font-weight: 300;
    color: var(--ink-soft);
    white-space: nowrap;
  }
  .back__mark {
    position: absolute;
    left: 34px;
    top: 84px;
    width: 176px;
    height: 176px;
    background: var(--mark-faint);
  }
  .contact {
    position: absolute;
    left: 226px;
    top: 188px;
    padding-left: 14px;
    border-left: 1.5px solid var(--ink-white);
    list-style: none;
    font-size: 14px;
    font-weight: 300;
    line-height: 1.3;
    white-space: nowrap;
  }
  .contact__item { display: flex; gap: 8px; align-items: flex-start; }
  .contact__item svg { width: 13px; height: 13px; margin-top: 3px; flex: none; }
  .contact__indent { padding-left: 21px; }
</style>
</head>
<body>

  <section class="card card--front" aria-label="Business card front">
    <div class="brand">
      <span class="brand__square"></span>
      <span class="brand__name">Quiet Harbour</span>
    </div>
    <p class="front__tagline">Tourism Marketing &amp; Representation</p>
    <p class="front__web">
      <svg viewBox="0 0 16 16" aria-hidden="true"><circle cx="8" cy="8" r="7.5" fill="#1a78b8"/><ellipse cx="8" cy="8" rx="3" ry="7" fill="none" stroke="#fff" stroke-width="1"/><line x1="1" y1="8" x2="15" y2="8" stroke="#fff" stroke-width="1"/></svg>
      www.quietharbour.com.au
    </p>
  </section>

  <section class="card card--back" aria-label="Business card back">
    <span class="back__tab"></span>
    <div class="back__heading">
      <h1 class="back__name">Odette Farrow</h1>
      <p class="back__role">Director</p>
    </div>
    <p class="back__tagline">Tourism Marketing &amp; Representation</p>
    <span class="back__mark"></span>
    <ul class="contact">
      <li class="contact__item">
        <svg viewBox="0 0 14 14" aria-hidden="true"><path d="M7 1 L13 7 H11 V13 H8.5 V9 H5.5 V13 H3 V7 H1 Z" fill="#fff"/></svg>
        57 Wendlow Terrace, Prahran, Victoria
      </li>
      <li class="contact__indent">3181 Australia</li>
      <li class="contact__item">
        <svg viewBox="0 0 14 14" aria-hidden="true"><path d="M3 1 L5.5 3.5 L4.2 5.5 C5 7.3 6.7 9 8.5 9.8 L10.5 8.5 L13 11 L11 13 C6 12.5 1.5 8 1 3 Z" fill="#fff"/></svg>
        +61 428306172
      </li>
      <li class="contact__item">
        <svg viewBox="0 0 14 14" aria-hidden="true"><rect x="1" y="3" width="12" height="8" fill="none" stroke="#fff" stroke-width="1.2"/><path d="M1 3 L7 8 L13 3" fill="none" stroke="#fff" stroke-width="1.2"/></svg>
        odette@quietharbour.com.au
      </li>
    </ul>
  </section>

</body>
</html>
```